Real Estate "For Sale" Sign for construction company

We need a sign that we can use to hang on a post and place on the road when we sell a property. The sign will be simple and will need to mainly feature our logo (files attached), as well as the words "For Sale", and then our phone number "(555) 617 3489". The sign will hang on a post that'll look something like the attached picture.

Target Market(s)

Home buyers

Industry/Entity Type

Real Estate

Font styles to use
Serif
Sans Serif

Colors
0054AA
0677BA
7BADD7
CADEEF
E8F1F8
0094D4
00A9DD
6FCCEA
C7EBF8
E9F6FB

Requirements
Must have
• For Sale & our phone number

```html
<!DOCTYPE html>
<html lang="en">
<head>
<meta charset="utf-8">
<title>Highland Crest Properties — For Sale</title>
<link rel="stylesheet" href="https://fonts.googleapis.com/css2?family=Lexend:wght@400&family=Playfair+Display:wght@800&display=swap">
<style>
  :root {
    --sky-deep: #0052a3;
    --sky-band: #9fdaf5;
    --sky-pale: #cbe9f9;
    --navy: #253a7a;
    --brand-blue: #1677ba;
  }
  html, body {
    margin: 0;
    padding: 0;
    width: 960px;
    height: 1200px;
    overflow: hidden;
    background: var(--sky-pale);
  }
  .sign {
    position: relative;
    width: 960px;
    height: 1200px;
    background: var(--sky-pale);
    overflow: hidden;
  }
  .sign__backdrop {
    position: absolute;
    inset: 0;
  }
  .brand {
    position: absolute;
    left: 0;
    width: 960px;
    top: 170px;
    text-align: center;
    color: var(--brand-blue);
    font-family: "Lexend", sans-serif;
    font-weight: 400;
  }
  .brand__name {
    font-size: 50px;
    line-height: 1;
    letter-spacing: 0.5px;
    margin: 0;
  }
  .brand__tagline {
    font-size: 20px;
    letter-spacing: 16px;
    margin: 16px 0 0 16px;
    line-height: 1;
  }
  .headline {
    position: absolute;
    left: 0;
    top: 0;
    width: 960px;
    height: 1200px;
  }
  .headline text {
    font-family: "Playfair Display", serif;
    font-weight: 800;
    fill: var(--navy);
  }
  .contact-bar {
    position: absolute;
    left: 0;
    top: 1026px;
    width: 960px;
    height: 129px;
    background: var(--navy);
    display: flex;
    align-items: center;
    justify-content: center;
    gap: 26px;
    color: var(--sky-pale);
  }
  .contact-bar__icon {
    width: 56px;
    height: 56px;
  }
  .contact-bar__phone {
    font-family: "Lexend", sans-serif;
    font-weight: 400;
    font-size: 62px;
    letter-spacing: 0.5px;
    line-height: 1;
  }
</style>
</head>
<body>
<main class="sign">
  <svg class="sign__backdrop" viewBox="0 0 960 1200" aria-hidden="true">
    <path d="M0 0 H960 V88 C700 30 300 40 0 181 Z" fill="var(--sky-deep)"/>
    <path d="M0 181 C300 40 700 30 960 88 L960 88 C640 70 220 150 0 352 Z" fill="var(--sky-band)"/>
    <path d="M104 970 Q480 966 856 970 Q480 974 104 970 Z" fill="var(--navy)"/>
  </svg>

  <header class="brand">
    <p class="brand__name">Highland Crest</p>
    <p class="brand__tagline">PROPERTIES</p>
  </header>

  <svg class="headline" viewBox="0 0 960 1200" role="heading" aria-level="1" aria-label="For Sale">
    <text x="186" y="617" font-size="350" textLength="612" lengthAdjust="spacingAndGlyphs">FOR</text>
    <text x="106" y="906" font-size="350" textLength="767" lengthAdjust="spacingAndGlyphs">SALE</text>
  </svg>

  <footer class="contact-bar">
    <svg class="contact-bar__icon" viewBox="0 0 56 56" fill="none" stroke="currentColor" stroke-width="2" stroke-linecap="round" stroke-linejoin="round" aria-hidden="true">
      <path d="M14 6 c-4 2 -9 6 -8 13 c2 12 16 28 29 31 c6 1 10 -3 12 -6 c1 -2 0 -3 -2 -5 l-6 -5 c-2 -1 -3 -1 -4 0 l-3 3 c-6 -2 -11 -8 -13 -13 l3 -3 c1 -1 1 -3 0 -4 l-5 -7 c-1 -2 -2 -2 -3 -4 z"/>
      <path d="M32 10 a14 14 0 0 1 14 14"/>
      <path d="M32 17 a7 7 0 0 1 7 7"/>
    </svg>
    <span class="contact-bar__phone">(555) 617 3489</span>
  </footer>
</main>
</body>
</html>
```